New Stationary Design

Harlow Voltworks Ltd have acquired Brackmoor Kitchen Supply Ltd. We will be retaining the Brackmoor Kitchen Supply Ltd name and require new letter head, compliment slips & business card designs.

I have attached the existing Harlow Voltworks letterhead to show our current image/brand. I do not wish to change this substantially & imagine maybe a swap of colours from Red logo to Blue, and the title & footer bars maybe in Red. That said, I'm open to subtle changes in the overall design & to maybe modernise it and if we like them, we would probably ask the Designer to update the changes to reflect them on the Harlow Voltworks stationary as well.

We will be able to get some proper high def images for Catering equipment to include, but for the time being if desingers can use any standard stock images for initial presentation.

The logo will be printed onto a Red van so somehow we need to be able to modify it for that use.

Brackmoor Kitchen Supply Ltd. Correspondence Address: 47 Lower Fenwick Road, Northampton. NN3 8QX. Tel 01604 738 092. Fax 01604 738 416. No website currently. Registered No: 05817264. Vat No: 418 3052 96. Company Registered Address: 22 Calloway Close, Leicester. LE2 7RN. We would also like to mention that we have Regional Service Centres also based in Leicester & Stockport.

Business Cards would be for;

Owen Pritchard, Director. owen.pritchard@brackmoorkitchensupply.co.uk

Trevor Holbrook, Operations Manager. trevor.holbrook@brackmoorkitchensupply.co.uk

Neil Dunmore, Service Manager. neil.dunmore@brackmoorkitchensupply.co.uk

Simon Ketley, Business Development Manager. simon.ketley@brackmoorkitchensupply.co.uk

We would also like the letter head to include the 'Flue Sure' logo & our registration Number: To be confirmed. Also the Electrical Contractors logo & the words Wiring Trades Guild underneath so people know what it means. See www.wtgx.co.uk

Target Market(s)

Businesses who use Catering Equipment such as Cookers. fridges etc. Hence, Care Homes, Hospitals, Restaurants etc

Industry/Entity Type

Business

Requirements
Must have
• Resemblance to existing Harlow Voltworks brand, although maybe with some changes & modernisation.
Nice to have
• Could maybe have some 'icons' for the type of equipment we sell instead of photos. Ie Cookers, Ovens, Fridges, Microwaves, Dishwashers, as well as kithen cateringtabling, commercial extraction hoods etc.

```html
<!DOCTYPE html>
<html lang="en">
<head>
<meta charset="utf-8">
<title>Brackmoor Kitchen Supply Ltd – Stationery</title>
<link rel="stylesheet" href="https://fonts.googleapis.com/css2?family=Arimo:wght@400;700&display=swap">
<style>
  :root {
    --navy: #1b4f72;
    --red: #e8323f;
    --paper: #ffffff;
    --backdrop: #4a3024;
    --ink-light: #ffffff;
  }
  * { margin: 0; padding: 0; box-sizing: border-box; }
  html, body { width: 1200px; height: 900px; overflow: hidden; }
  body { background: var(--backdrop); font-family: "Arimo", Arial, sans-serif; position: relative; }

  .sheet { position: absolute; background: var(--paper); }

  /* Letterhead */
  .letterhead { left: 24px; top: 14px; width: 609px; height: 860px; }
  .letterhead .header-bar { position: absolute; left: 0; top: 0; width: 100%; height: 70px; background: var(--navy); }
  .letterhead .footer-bar {
    position: absolute; left: 0; bottom: 0; width: 100%; height: 70px; background: var(--navy);
    color: var(--ink-light); font-size: 11.5px; line-height: 13.5px; text-align: center; padding-top: 8px;
  }

  .brand { position: absolute; display: flex; align-items: center; color: var(--red); font-weight: 700; }
  .brand .mark { background: var(--red); flex: none; }
  .brand .name { line-height: 1.1; }

  .letterhead .brand { left: 24px; top: 82px; gap: 10px; font-size: 24px; }
  .letterhead .brand .mark { width: 40px; height: 40px; }

  /* Business card front */
  .card-front { left: 671px; top: 158px; width: 480px; height: 307px; }
  .card-front .band { position: absolute; left: 0; width: 100%; height: 32px; background: var(--navy); }
  .card-front .band.top { top: 0; }
  .card-front .band.bottom { bottom: 0; }
  .card-front .brand { left: 84px; top: 110px; gap: 14px; font-size: 36px; }
  .card-front .brand .mark { width: 60px; height: 60px; }

  /* Business card back */
  .card-back { left: 671px; top: 482px; width: 480px; height: 308px; background: var(--navy); }
  .card-back .logo-panel { position: absolute; left: 29px; top: 0; width: 196px; height: 100%; background: var(--paper); }
  .card-back .brand { left: 10px; top: 116px; gap: 8px; font-size: 20px; }
  .card-back .brand .mark { width: 26px; height: 26px; }

  .staff-list { position: absolute; left: 237px; top: 24px; color: var(--ink-light); list-style: none; }
  .staff { margin-bottom: 14px; }
  .staff .person { font-size: 16px; font-weight: 700; line-height: 17px; }
  .staff .role { font-size: 13.5px; line-height: 16px; }
  .staff .email { font-size: 10.5px; line-height: 13px; margin-top: 8px; }
</style>
</head>
<body>

  <section class="sheet letterhead">
    <div class="header-bar"></div>
    <div class="brand">
      <span class="mark"></span>
      <span class="name">Brackmoor Kitchen<br>Supply Ltd</span>
    </div>
    <footer class="footer-bar">
      Brackmoor Kitchen Supply Ltd. Correspondence Address: 47 Lower Fenwick Road, Northampton. NN3 8QX.<br>
      Tel 01604 738 092. Fax 01604 738 416.&nbsp; Registered No: 05817264. Vat No: 418 3052 96<br>
      Company Registered Address: 22 Calloway Close, Leicester. LE2 7RN<br>
      Regional Service Centres are based in Leicester &amp; Stockport.
    </footer>
  </section>

  <section class="sheet card-front">
    <div class="band top"></div>
    <div class="brand">
      <span class="mark"></span>
      <span class="name">Brackmoor Kitchen<br>Supply Ltd</span>
    </div>
    <div class="band bottom"></div>
  </section>

  <section class="sheet card-back">
    <div class="logo-panel">
      <div class="brand">
        <span class="mark"></span>
        <span class="name">Brackmoor Kitchen<br>Supply Ltd</span>
      </div>
    </div>
    <ul class="staff-list">
      <li class="staff">
        <div class="person">Owen Pritchard</div>
        <div class="role">Director</div>
        <div class="email">owen.pritchard@brackmoorkitchensupply.co.uk</div>
      </li>
      <li class="staff">
        <div class="person">Trevor Holbrook</div>
        <div class="role">Operations Manager</div>
        <div class="email">trevor.holbrook@brackmoorkitchensupply.co.uk</div>
      </li>
      <li class="staff">
        <div class="person">Neil Dunmore</div>
        <div class="role">Service Manager</div>
        <div class="email">neil.dunmore@brackmoorkitchensupply.co.uk</div>
      </li>
      <li class="staff">
        <div class="person">Simon Ketley</div>
        <div class="role">Business Development Manager</div>
        <div class="email">simon.ketley@brackmoorkitchensupply.co.uk</div>
      </li>
    </ul>
  </section>

</body>
</html>
```